Business Card for my New Brokerage

Looking to get a business card design for my new Real Estate Brokerage.
I want it with Picture, Phone Number, Email, Website, Office Address
Name and Designation. Please add logo too.

Target Market(s)

Real Estate Investors or Home Buyers

Industry/Entity Type

Real Estate

Contact Information for Business Card

Name, Email, Phone Number, website, email, office address

Colors
EB3D1F
EC4F4E
F09395
F8D3D4
FCEDEE

Requirements
Must have
• Minimalistic, Clean, Modern, Photo
Nice to have
• White and Red Colors

```html
<!DOCTYPE html>
<html lang="en">
<head>
<meta charset="utf-8">
<title>Ember Realty Inc – Business Card</title>
<link href="https://fonts.googleapis.com/css2?family=Arimo:wght@400;700&display=swap" rel="stylesheet">
<style>
  :root {
    --backdrop: #e6e6e4;
    --card: #2b2b2d;
    --card-dark: #1c1c1e;
    --art-light: #48484b;
    --red: #d90f0f;
    --edge-red: #b10000;
    --text-light: #e9e9e9;
    --divider: #bdbdbd;
  }
  * { margin: 0; padding: 0; box-sizing: border-box; }
  html, body { width: 1200px; height: 801px; overflow: hidden; }
  body {
    background: var(--backdrop);
    font-family: "Arimo", Arial, sans-serif;
    position: relative;
  }
  .card {
    position: absolute;
    top: 246px;
    width: 540px;
    height: 308px;
    background: linear-gradient(160deg, #313133 0%, var(--card) 60%, #252527 100%);
    border-bottom: 4px solid var(--edge-red);
    box-shadow: 0 10px 24px rgba(0,0,0,.25);
    overflow: hidden;
  }
  .card--front { left: 40px; }
  .card--back { left: 620px; }

  .brand-name {
    position: absolute;
    color: var(--red);
    font-weight: 700;
    line-height: 1;
    white-space: nowrap;
  }
  .card--front .brand-name {
    left: 0; right: 0;
    top: 64px;
    text-align: center;
    font-size: 30px;
  }
  .card--back .brand-name {
    right: 52px;
    top: 92px;
    font-size: 34px;
  }

  .person {
    position: absolute;
    right: 285px;
    top: 170px;
    text-align: right;
  }
  .person__name { color: var(--red); font-weight: 700; font-size: 14px; letter-spacing: .4px; }
  .person__role { color: var(--text-light); font-size: 13px; margin-top: 4px; }

  .divider {
    position: absolute;
    left: 270px;
    top: 158px;
    width: 1px;
    height: 62px;
    background: var(--divider);
  }

  .contacts {
    position: absolute;
    left: 288px;
    top: 158px;
    list-style: none;
  }
  .contacts__item {
    display: flex;
    align-items: center;
    gap: 8px;
    color: var(--text-light);
    font-size: 12.5px;
    height: 21px;
  }
  .contacts__icon { width: 12px; height: 12px; flex: none; }

  .address {
    position: absolute;
    left: 0; right: 0;
    bottom: 36px;
    text-align: center;
    color: var(--text-light);
    font-size: 13px;
  }

  .house-art {
    position: absolute;
    left: 0;
    bottom: 0;
    width: 440px;
    height: 158px;
    background: linear-gradient(110deg, var(--card-dark) 0%, #2a2a2c 55%, var(--art-light) 100%);
  }
</style>
</head>
<body>

<section class="card card--front" aria-label="Business card front">
  <p class="brand-name">EMBER REALTY INC</p>

  <div class="person">
    <p class="person__name">DANIEL MORROW</p>
    <p class="person__role">Manager</p>
  </div>

  <div class="divider"></div>

  <ul class="contacts">
    <li class="contacts__item">
      <svg class="contacts__icon" viewBox="0 0 12 12"><circle cx="6" cy="6" r="6" fill="var(--red)"/><path d="M3.6 3.2c.4-.3.8-.3 1 .1l.5 1c.1.3 0 .5-.2.7l-.3.3c.3.7.8 1.2 1.5 1.5l.3-.3c.2-.2.4-.3.7-.2l1 .5c.4.2.4.6.1 1-.6.7-1.6.7-2.8-.1C4.3 7 3.5 6.1 3.2 5.2c-.3-.8-.1-1.5.4-2z" fill="#fff"/></svg>
      <span>123-456-7800</span>
    </li>
    <li class="contacts__item">
      <svg class="contacts__icon" viewBox="0 0 12 12"><rect x="0.5" y="2" width="11" height="8" rx="1" fill="var(--red)"/><path d="M1 2.6l5 3.6 5-3.6" stroke="#fff" stroke-width="1" fill="none"/></svg>
      <span>contact@emberrealty.com</span>
    </li>
    <li class="contacts__item">
      <svg class="contacts__icon" viewBox="0 0 12 12"><circle cx="6" cy="6" r="5.5" fill="var(--red)"/><g stroke="#fff" stroke-width=".8" fill="none"><circle cx="6" cy="6" r="4"/><ellipse cx="6" cy="6" rx="1.8" ry="4"/><path d="M2 6h8"/></g></svg>
      <span>www.emberrealty.com</span>
    </li>
  </ul>

  <p class="address">Your address, city, state, ZIP 0000</p>
</section>

<section class="card card--back" aria-label="Business card back">
  <div class="house-art" role="img" aria-label="Dark house roof illustration with window"></div>
  <p class="brand-name">EMBER REALTY INC</p>
</section>

</body>
</html>
```